Personal Trainer and Corporate Health Business

I need a business card for a new company I'm starting in Australia called "Brisk Vigour Outreach" I will be providing a Personal training service as well as corporate health in companies.
The service provided is to help promote an active and healthy lifstyle.
The design should communicate a healthy lifestyle and also the benefits that this can have on a personal level and in the corporate environment and the benefits that flow from that.

Target Market(s)

Members of the public and Corporate

Industry/Entity Type

Environment

Requirements
Must have
• Company logo attached
Look and feel fresh and modern

Tag line: "Briskly championing a more vigorous life"

Colin Varga
Managing Director

m: 0412 657 394
e: colin@briskvigouroutreach.com.au

www.briskvigouroutreach.com.au
Nice to have
• Can be 1 or 2 sided

```html
<!DOCTYPE html>
<html lang="en">
<head>
<meta charset="utf-8">
<title>Brisk Vigour Outreach – Business Card</title>
<link rel="stylesheet" href="https://fonts.googleapis.com/css2?family=Arimo:wght@400;700&family=Schoolbell&display=swap">
<style>
  :root {
    --stage: #2b2b2b;
    --card-dark: #242424;
    --card-light: #ffffff;
    --brand-blue: #0b5fad;
    --brand-green: #9ccb3b;
    --text-light: #f2f2f2;
  }
  * { box-sizing: border-box; margin: 0; padding: 0; }
  html, body { width: 1200px; height: 1200px; overflow: hidden; }
  body {
    background: var(--stage);
    font-family: "Arimo", Arial, sans-serif;
    display: flex;
    flex-direction: column;
    align-items: center;
    justify-content: center;
    gap: 60px;
  }
  .card {
    position: relative;
    width: 900px;
    height: 514px;
    overflow: hidden;
    box-shadow: 0 18px 40px rgba(0,0,0,0.55);
  }

  /* Brand name lockup */
  .brand {
    display: flex;
    align-items: center;
    justify-content: center;
    gap: 16px;
  }
  .brand-dot {
    width: 34px; height: 34px;
    border-radius: 50%;
    background: var(--brand-green);
  }
  .brand-name {
    font-family: "Arimo", Arial, sans-serif;
    font-weight: 700;
    font-size: 48px;
    letter-spacing: 1px;
    color: var(--brand-blue);
  }

  /* Card back */
  .card-back { background: var(--card-dark); }
  .card-back .brand {
    position: absolute;
    left: 0; right: 0; top: 150px;
  }
  .tagline-band {
    position: absolute;
    left: 0; right: 0; bottom: 0;
    height: 150px;
    background: var(--brand-blue);
    border-top: 12px solid var(--brand-green);
    display: flex;
    align-items: center;
    justify-content: center;
  }
  .tagline {
    font-family: "Schoolbell", cursive;
    font-size: 34px;
    letter-spacing: 3px;
    color: var(--text-light);
    white-space: nowrap;
  }

  /* Card front */
  .card-front { background: var(--card-dark); }
  .front-header {
    position: absolute;
    left: 0; right: 0; top: 0;
    height: 250px;
    background: var(--card-light);
    display: flex;
    align-items: center;
    justify-content: center;
  }
  .front-stripes {
    position: absolute;
    left: 0; right: 0; top: 250px;
  }
  .stripe { height: 9px; }
  .stripe-green { background: var(--brand-green); }
  .stripe-blue { background: var(--brand-blue); }
  .stripe-gap { height: 5px; background: var(--card-light); }

  .contact-block {
    position: absolute;
    left: 120px; top: 300px;
    color: var(--text-light);
  }
  .person {
    display: flex;
    align-items: baseline;
    gap: 14px;
    margin-bottom: 12px;
    line-height: 1.1;
  }
  .person-name {
    font-size: 46px;
    letter-spacing: 3px;
    color: var(--brand-green);
  }
  .person-divider { font-size: 40px; color: var(--text-light); }
  .person-role {
    font-size: 28px;
    letter-spacing: 2px;
    color: var(--brand-blue);
  }
  .contact-list { list-style: none; padding-left: 70px; }
  .contact-item {
    display: flex;
    align-items: center;
    gap: 18px;
    font-size: 28px;
    letter-spacing: 1.5px;
    line-height: 42px;
  }
  .contact-icon { width: 30px; height: 30px; flex: none; }
</style>
</head>
<body>

  <section class="card card-back" aria-label="Business card back">
    <div class="brand">
      <span class="brand-dot"></span>
      <span class="brand-name">BRISK VIGOUR OUTREACH</span>
    </div>
    <div class="tagline-band">
      <p class="tagline">"Briskly championing a more vigorous life"</p>
    </div>
  </section>

  <section class="card card-front" aria-label="Business card front">
    <div class="front-header">
      <div class="brand">
        <span class="brand-dot"></span>
        <span class="brand-name">BRISK VIGOUR OUTREACH</span>
      </div>
    </div>
    <div class="front-stripes">
      <div class="stripe stripe-green"></div>
      <div class="stripe-gap"></div>
      <div class="stripe stripe-blue"></div>
      <div class="stripe-gap"></div>
      <div class="stripe stripe-green"></div>
    </div>

    <div class="contact-block">
      <div class="person">
        <span class="person-name">Colin Varga</span>
        <span class="person-divider">|</span>
        <span class="person-role">Managing Director</span>
      </div>
      <ul class="contact-list">
        <li class="contact-item">
          <svg class="contact-icon" viewBox="0 0 30 30" aria-hidden="true">
            <rect x="1" y="1" width="28" height="28" rx="3" fill="#0b5fad"/>
            <path d="M10 7c-2 1-3 3-2 6 2 5 5 8 10 10 3 1 5 0 6-2l-3-3-3 2c-3-1-5-3-6-6l2-3z" fill="#fff"/>
          </svg>
          <span>0412 657 394</span>
        </li>
        <li class="contact-item">
          <svg class="contact-icon" viewBox="0 0 30 30" aria-hidden="true">
            <rect x="1" y="5" width="28" height="20" rx="2" fill="#0b5fad"/>
            <path d="M2 6l13 11L28 6" fill="none" stroke="#fff" stroke-width="2"/>
          </svg>
          <span>colin@briskvigouroutreach.com.au</span>
        </li>
        <li class="contact-item">
          <svg class="contact-icon" viewBox="0 0 30 30" aria-hidden="true">
            <g fill="none" stroke="#0b5fad" stroke-width="2">
              <circle cx="15" cy="15" r="13"/>
              <ellipse cx="15" cy="15" rx="6" ry="13"/>
              <path d="M2 15h26M4 8h22M4 22h22"/>
            </g>
          </svg>
          <span>www.briskvigouroutreach.com.au</span>
        </li>
      </ul>
    </div>
  </section>

</body>
</html>
```